Step and Repeat Backdrop for wedding reception photo booth

Would like to have a Step and Repeat Backdrop (8 foot high by 10 foot wide) that incorporates the wedding logo (attached) and the names Elena and Gavin. Background should be white, and wedding colors are burgundy and gold. Show me creativity :-) I have included some random samples.

```html
<!DOCTYPE html>
<html lang="en">
<head>
<meta charset="utf-8">
<title>Elena &amp; Gavin — Step and Repeat Backdrop</title>
<link rel="stylesheet" href="https://fonts.googleapis.com/css2?family=Cagliostro&family=Playfair+Display:wght@600&display=swap">
<style>
  :root {
    --page-bg: #e9e9e9;
    --page-glow: #f7f7f7;
    --banner-bg: #ffffff;
    --gold: #b08d3e;
    --gold-light: #d8bd72;
    --gold-dark: #94722a;
  }
  * { margin: 0; padding: 0; box-sizing: border-box; }
  html, body { width: 1200px; height: 764px; overflow: hidden; }
  body {
    background: radial-gradient(ellipse at center, var(--page-glow) 0%, var(--page-bg) 75%);
    position: relative;
  }
  .backdrop {
    position: absolute;
    left: 160px; top: 30px;
    width: 880px; height: 704px;
    background: var(--banner-bg);
    box-shadow: 0 2px 10px rgba(0,0,0,0.08);
  }
  .repeat-item {
    position: absolute;
    transform: translate(-50%, -50%);
    color: var(--gold);
    white-space: nowrap;
    line-height: 1;
  }
  .couple-name {
    font-family: "Cagliostro", sans-serif;
    font-size: 15px;
  }
  .monogram {
    font-family: "Playfair Display", serif;
    font-weight: 600;
    font-size: 26px;
    letter-spacing: -1px;
  }
  .centerpiece {
    position: absolute;
    left: 291px; top: 201px;
    width: 300px; height: 300px;
  }
  .centerpiece svg { position: absolute; inset: 0; width: 300px; height: 300px; }
  .arc-name {
    font-family: "Cagliostro", sans-serif;
    font-size: 23px;
    fill: var(--gold);
  }
  .center-monogram {
    font-family: "Playfair Display", serif;
    font-weight: 600;
    font-size: 32px;
    fill: var(--gold);
  }
</style>
</head>
<body>
<main class="backdrop">
  <!-- row 1 -->
  <span class="repeat-item monogram" style="left:75px;top:60px">E&amp;G</span>
  <span class="repeat-item couple-name" style="left:167px;top:60px">Elena &amp; Gavin</span>
  <span class="repeat-item monogram" style="left:258px;top:60px">E&amp;G</span>
  <span class="repeat-item couple-name" style="left:350px;top:60px">Elena &amp; Gavin</span>
  <span class="repeat-item monogram" style="left:441px;top:60px">E&amp;G</span>
  <span class="repeat-item couple-name" style="left:532px;top:60px">Elena &amp; Gavin</span>
  <span class="repeat-item monogram" style="left:624px;top:60px">E&amp;G</span>
  <span class="repeat-item couple-name" style="left:715px;top:60px">Elena &amp; Gavin</span>
  <span class="repeat-item monogram" style="left:807px;top:60px">E&amp;G</span>
  <!-- row 2 -->
  <span class="repeat-item couple-name" style="left:75px;top:144px">Elena &amp; Gavin</span>
  <span class="repeat-item monogram" style="left:167px;top:144px">E&amp;G</span>
  <span class="repeat-item couple-name" style="left:258px;top:144px">Elena &amp; Gavin</span>
  <span class="repeat-item monogram" style="left:350px;top:144px">E&amp;G</span>
  <span class="repeat-item couple-name" style="left:441px;top:144px">Elena &amp; Gavin</span>
  <span class="repeat-item monogram" style="left:532px;top:144px">E&amp;G</span>
  <span class="repeat-item couple-name" style="left:624px;top:144px">Elena &amp; Gavin</span>
  <span class="repeat-item monogram" style="left:715px;top:144px">E&amp;G</span>
  <span class="repeat-item couple-name" style="left:807px;top:144px">Elena &amp; Gavin</span>
  <!-- row 3 -->
  <span class="repeat-item monogram" style="left:75px;top:227px">E&amp;G</span>
  <span class="repeat-item couple-name" style="left:167px;top:227px">Elena &amp; Gavin</span>
  <span class="repeat-item monogram" style="left:258px;top:227px">E&amp;G</span>
  <span class="repeat-item monogram" style="left:624px;top:227px">E&amp;G</span>
  <span class="repeat-item couple-name" style="left:715px;top:227px">Elena &amp; Gavin</span>
  <span class="repeat-item monogram" style="left:807px;top:227px">E&amp;G</span>
  <!-- row 4 -->
  <span class="repeat-item couple-name" style="left:75px;top:310px">Elena &amp; Gavin</span>
  <span class="repeat-item monogram" style="left:167px;top:310px">E&amp;G</span>
  <span class="repeat-item couple-name" style="left:258px;top:310px">Elena &amp; Gavin</span>
  <span class="repeat-item couple-name" style="left:624px;top:310px">Elena &amp; Gavin</span>
  <span class="repeat-item monogram" style="left:715px;top:310px">E&amp;G</span>
  <span class="repeat-item couple-name" style="left:807px;top:310px">Elena &amp; Gavin</span>
  <!-- row 5 -->
  <span class="repeat-item monogram" style="left:75px;top:393px">E&amp;G</span>
  <span class="repeat-item couple-name" style="left:167px;top:393px">Elena &amp; Gavin</span>
  <span class="repeat-item monogram" style="left:258px;top:393px">E&amp;G</span>
  <span class="repeat-item monogram" style="left:624px;top:393px">E&amp;G</span>
  <span class="repeat-item couple-name" style="left:715px;top:393px">Elena &amp; Gavin</span>
  <span class="repeat-item monogram" style="left:807px;top:393px">E&amp;G</span>
  <!-- row 6 -->
  <span class="repeat-item couple-name" style="left:75px;top:476px">Elena &amp; Gavin</span>
  <span class="repeat-item monogram" style="left:167px;top:476px">E&amp;G</span>
  <span class="repeat-item couple-name" style="left:258px;top:476px">Elena &amp; Gavin</span>
  <span class="repeat-item couple-name" style="left:624px;top:476px">Elena &amp; Gavin</span>
  <span class="repeat-item monogram" style="left:715px;top:476px">E&amp;G</span>
  <span class="repeat-item couple-name" style="left:807px;top:476px">Elena &amp; Gavin</span>
  <!-- row 7 -->
  <span class="repeat-item monogram" style="left:75px;top:560px">E&amp;G</span>
  <span class="repeat-item couple-name" style="left:167px;top:560px">Elena &amp; Gavin</span>
  <span class="repeat-item monogram" style="left:258px;top:560px">E&amp;G</span>
  <span class="repeat-item couple-name" style="left:350px;top:560px">Elena &amp; Gavin</span>
  <span class="repeat-item monogram" style="left:441px;top:560px">E&amp;G</span>
  <span class="repeat-item couple-name" style="left:532px;top:560px">Elena &amp; Gavin</span>
  <span class="repeat-item monogram" style="left:624px;top:560px">E&amp;G</span>
  <span class="repeat-item couple-name" style="left:715px;top:560px">Elena &amp; Gavin</span>
  <span class="repeat-item monogram" style="left:807px;top:560px">E&amp;G</span>
  <!-- row 8 -->
  <span class="repeat-item couple-name" style="left:75px;top:643px">Elena &amp; Gavin</span>
  <span class="repeat-item monogram" style="left:167px;top:643px">E&amp;G</span>
  <span class="repeat-item couple-name" style="left:258px;top:643px">Elena &amp; Gavin</span>
  <span class="repeat-item monogram" style="left:350px;top:643px">E&amp;G</span>
  <span class="repeat-item couple-name" style="left:441px;top:643px">Elena &amp; Gavin</span>
  <span class="repeat-item monogram" style="left:532px;top:643px">E&amp;G</span>
  <span class="repeat-item couple-name" style="left:624px;top:643px">Elena &amp; Gavin</span>
  <span class="repeat-item monogram" style="left:715px;top:643px">E&amp;G</span>
  <span class="repeat-item couple-name" style="left:807px;top:643px">Elena &amp; Gavin</span>

  <div class="centerpiece">
    <svg viewBox="0 0 300 300" role="img" aria-label="Gold leafy ornamental wreath framing the couple's names">
      <defs>
        <linearGradient id="wreath-gold" x1="0" y1="0" x2="1" y2="1">
          <stop offset="0" stop-color="var(--gold-light)"/>
          <stop offset="0.5" stop-color="var(--gold)"/>
          <stop offset="1" stop-color="var(--gold-dark)"/>
        </linearGradient>
      </defs>
      <circle cx="150" cy="150" r="118" fill="none" stroke="url(#wreath-gold)" stroke-width="16" opacity="0.85"/>
    </svg>
    <svg viewBox="0 0 300 300">
      <defs>
        <path id="arc-top" d="M 66,150 A 84,84 0 0 1 234,150"/>
        <path id="arc-bottom" d="M 56,150 A 94,94 0 0 0 244,150"/>
      </defs>
      <text class="arc-name"><textPath href="#arc-top" startOffset="50%" text-anchor="middle">Elena &amp; Gavin</textPath></text>
      <text class="arc-name"><textPath href="#arc-bottom" startOffset="50%" text-anchor="middle">Elena &amp; Gavin</textPath></text>
      <text class="center-monogram" x="150" y="161" text-anchor="middle">E&amp;G</text>
    </svg>
  </div>
</main>
</body>
</html>
```